SHIELDLINE LEGAL

I'm virtually ready to launch my site, but I have a number of edits and modifications that need to be implemented. More importantly, I'm always looking to improve my site, particularly now that I am making my proverbial "FIRST IMPRESSION." Thus, I'm willing to see if there is someone who can add creativity and perhaps improve what I already have, particularly on the All Important Front Page.

Need extra days to review

```html
<!DOCTYPE html>
<html lang="en">
<head>
<meta charset="utf-8">
<title>Shieldline Legal</title>
<link href="https://fonts.googleapis.com/css2?family=Ubuntu:wght@300;400;500;700&family=Roboto:wght@300;400;500;700&display=swap" rel="stylesheet">
<style>
:root{
  --navy:#0d2752;
  --navy-deep:#0a1a3a;
  --red:#b0121b;
  --light:#eef1f6;
  --white:#ffffff;
  --muted:#5b6577;
  --lavender:#c9cbee;
}
*{box-sizing:border-box;margin:0;padding:0}
html,body{width:1200px;height:4355px;overflow:hidden}
body{position:relative;font-family:'Roboto',sans-serif;color:var(--navy);background:var(--white)}
.abs{position:absolute}
.head{font-family:'Ubuntu',sans-serif}
section,header,footer{position:absolute;left:0;width:1200px}

/* hero */
.hero{top:0;height:764px}
.hero-photo{position:absolute;inset:0;background:linear-gradient(110deg,#3a3d44 0%,#2b2d33 40%,#4a4c52 70%,#2e3036 100%)}
.hero-shade{position:absolute;inset:0;background:rgba(15,18,28,.45)}
.topbar{top:0;height:34px;font-size:13px;color:#fff}
.topbar span{position:absolute;top:9px;display:flex;align-items:center;gap:6px;white-space:nowrap}
.social{display:inline-block;width:13px;height:13px;border:1.5px solid #fff;border-radius:2px}
.nav{top:30px;left:88px;width:1027px;height:88px;background:#fff;border-radius:4px}
.nav-brand{position:absolute;left:56px;top:17px;display:flex;align-items:center;gap:10px;font-family:'Ubuntu',sans-serif;font-size:15px;font-weight:500;color:var(--navy);white-space:nowrap}
.dot{display:inline-block;flex:none;border-radius:50%;background:var(--navy)}
.nav a{position:absolute;top:36px;font-size:14px;color:var(--navy);text-decoration:none}
.eyebrow-hero{top:324px;width:1200px;text-align:center;color:#fff;font-size:15px;letter-spacing:.5px}
.hero h1{position:absolute;top:345px;width:1200px;text-align:center;color:#fff;font-family:'Ubuntu',sans-serif;font-weight:300;font-size:82px;line-height:96px}
.btn-red{position:absolute;background:var(--red);color:#fff;font-weight:700;font-size:16px;display:flex;align-items:center;justify-content:center;gap:14px;border-radius:2px}

/* shared */
.label{position:absolute;width:1200px;text-align:center;font-size:13px;color:var(--red);text-decoration:underline;text-underline-offset:4px;letter-spacing:.3px}
.title{position:absolute;width:1200px;text-align:center;font-family:'Ubuntu',sans-serif;font-weight:500;font-size:44px;color:var(--navy)}

/* services */
.services{top:764px;height:684px;background:var(--light)}
.card{position:absolute;top:220px;width:324px;height:253px;background:#fff;box-shadow:0 3px 10px rgba(0,0,0,.08)}
.card-photo{position:absolute;left:18px;top:0;width:290px;height:162px}
.card small{position:absolute;top:183px;width:100%;text-align:center;font-size:12px;color:var(--red)}
.card h3{position:absolute;top:200px;width:100%;text-align:center;font-family:'Ubuntu',sans-serif;font-weight:400;font-size:28px;color:var(--navy)}
.tagline{position:absolute;top:528px;width:1200px;text-align:center;font-size:18px;color:var(--muted)}
.btn-white{position:absolute;left:487px;top:574px;width:219px;height:65px;background:#fff;color:var(--red);font-family:'Ubuntu',sans-serif;font-weight:500;font-size:24px;display:flex;align-items:center;justify-content:center;gap:22px;box-shadow:0 2px 8px rgba(0,0,0,.06)}

/* about */
.about{top:1448px;height:557px}
.about-bg{position:absolute;inset:0;background:linear-gradient(90deg,#1b2230,#2a3140 50%,#1c2230)}
.about-shade{position:absolute;inset:0;background:rgba(10,14,24,.55)}
.back-card{position:absolute;left:100px;top:78px;width:400px;height:370px;background:#2d3140;border-radius:22px;transform:rotate(-5deg);border-right:14px solid var(--navy)}
.about-photo{position:absolute;left:112px;top:88px;width:382px;height:370px;border-radius:22px;background:linear-gradient(135deg,#c8ccd6,#8a93a8 60%,#2a3556)}
.about-text{position:absolute;left:614px;color:#fff}
.about h2{font-family:'Ubuntu',sans-serif;font-weight:700;font-size:44px;line-height:54px}

/* why */
.why{top:2005px;height:709px;background:#fff}
.ring{position:absolute;border-radius:50%}
.feat-icon{position:absolute;width:66px;height:66px;margin:-33px 0 0 -33px;border-radius:50%;background:var(--navy);border:4px solid #fff;box-shadow:0 0 0 1px #d5d8ea;display:flex;align-items:center;justify-content:center}
.feat{position:absolute;width:300px}
.feat h4{font-family:'Ubuntu',sans-serif;font-weight:400;font-size:21px;color:var(--navy)}
.feat p{font-size:13.5px;line-height:20px;color:var(--muted);margin-top:4px}
.feat.l{text-align:right}

/* testimonials */
.reviews{top:2714px;height:554px}
.reviews-bg{position:absolute;inset:0;background:linear-gradient(90deg,#1a1e28,#2b2f3a 50%,#181c26)}
.reviews-shade{position:absolute;inset:0;background:rgba(10,12,20,.5)}
.quote{position:absolute;top:189px;width:488px;height:190px;background:rgba(120,124,134,.45);border-radius:4px;color:#fff;padding:30px 20px}
.quote:after{content:"";position:absolute;left:36px;bottom:-16px;border:16px solid transparent;border-bottom:0;border-top-color:rgba(120,124,134,.45)}
.quote h3{font-family:'Ubuntu',sans-serif;font-weight:700;font-size:27px}
.quote p{font-size:15px;line-height:23px;margin-top:12px}
.person{position:absolute;top:409px;display:flex;align-items:center;gap:22px;color:#fff}
.avatar{width:68px;height:68px;border-radius:50%;background:linear-gradient(135deg,#f0e6dc,#b8a79a)}
.person b{display:block;font-family:'Ubuntu',sans-serif;font-size:22px}
.person span{font-size:15px}

/* contact */
.contact{top:3268px;height:1030px;background:#fff}
.contact-foot{position:absolute;left:0;top:620px;width:1200px;height:410px;background:linear-gradient(90deg,#1a1e28,#262a35 50%,#181c26)}
.curve{position:absolute;top:560px;left:0}
.contact-card{position:absolute;left:139px;top:225px;width:921px;height:458px;background:#fff;border-radius:14px;box-shadow:0 6px 24px rgba(0,0,0,.12);overflow:hidden}
.contact-photo{position:absolute;left:0;top:0;width:461px;height:458px;background:linear-gradient(135deg,#c9cdd4,#8c95a6 55%,#3b4558)}
.field{position:absolute;border:1px solid #cfd3db;border-radius:3px;font-size:12px;color:#8a909c;padding:8px 10px}
.send{position:absolute;left:510px;top:362px;width:360px;height:39px;background:var(--red);color:#fff;font-weight:700;font-size:15px;display:flex;align-items:center;justify-content:center;border-radius:3px}
.foot-brand{position:absolute;top:740px;width:1200px;display:flex;justify-content:center;align-items:center;gap:12px;color:#fff;font-family:'Ubuntu',sans-serif;font-weight:500;font-size:20px}
.foot-links a{position:absolute;top:850px;color:#fff;font-size:14px;font-weight:500;text-decoration:none}
.foot-rule{position:absolute;left:142px;top:898px;width:918px;height:1px;background:rgba(255,255,255,.3)}
.foot-item{position:absolute;top:935px;display:flex;align-items:center;gap:14px;color:#fff;font-size:12px;line-height:17px;white-space:nowrap}
.foot-item b{font-size:14px}
.ring-icon{width:58px;height:58px;border-radius:50%;border:2px solid #fff;display:flex;align-items:center;justify-content:center}
.vline{position:absolute;top:938px;width:1px;height:58px;background:rgba(255,255,255,.35)}
.bottombar{top:4298px;height:57px;background:var(--navy-deep);color:#fff}
.bottombar .soc{position:absolute;top:19px;width:26px;height:26px;border:1.5px solid #fff;border-radius:3px}
</style>
</head>
<body>

<header class="hero">
  <div class="hero-photo" role="img" aria-label="Lawyer reviewing documents at a laptop in an office"></div>
  <div class="hero-shade"></div>
  <div class="abs topbar" style="width:1200px">
    <span style="left:100px"><svg width="10" height="13" viewBox="0 0 10 13"><path d="M5 0a5 5 0 0 1 5 5c0 4-5 8-5 8S0 9 0 5a5 5 0 0 1 5-5z" fill="#fff"/><circle cx="5" cy="5" r="1.8" fill="#333"/></svg>48 Harbor Lane, Ridgeton</span>
    <span style="left:362px"><svg width="13" height="10" viewBox="0 0 13 10"><rect width="13" height="10" rx="1" fill="#fff"/><path d="M0 1l6.5 5L13 1" stroke="#333" fill="none"/></svg>hello@shieldline.com</span>
    <span style="left:578px"><svg width="11" height="11" viewBox="0 0 11 11"><path d="M2 0l2 3-1 1.5c.8 1.5 2 2.7 3.5 3.5L8 7l3 2-1 2C5 11 0 6 0 1z" fill="#fff"/></svg>555 - 014- 2288</span>
    <span style="left:975px;gap:22px"><i class="social"></i><i class="social"></i><i class="social"></i><i class="social"></i></span>
  </div>
  <nav class="abs nav">
    <div class="nav-brand"><span class="dot" style="width:54px;height:54px"></span>Shieldline Legal</div>
    <a style="left:274px">Home</a>
    <a style="left:387px">About Us</a>
    <a style="left:498px">Services</a>
    <a style="left:636px">Solutions</a>
    <a style="left:749px">Team</a>
    <a style="left:841px">Contact Us</a>
  </nav>
  <div class="abs eyebrow-hero">LEGAL SERVICES</div>
  <h1>Unlocking the Power<br>of Legal Protection</h1>
  <div class="btn-red" style="left:524px;top:592px;width:155px;height:42px">Contact us
    <svg width="18" height="12" viewBox="0 0 18 12"><path d="M0 6h16M11 1l5 5-5 5" stroke="#fff" stroke-width="2" fill="none"/></svg></div>
</header>

<section class="services">
  <div class="label" style="top:70px">OUR SERVICES</div>
  <h2 class="title" style="top:102px">Services We Provide</h2>
  <div class="card" style="left:85px"><div class="card-photo" role="img" aria-label="Judge with gavel" style="background:linear-gradient(135deg,#5a4a3e,#2a2320)"></div><small>OUR SERVICES</small><h3>Consultation</h3></div>
  <div class="card" style="left:436px"><div class="card-photo" role="img" aria-label="Lawyer in a client meeting" style="background:linear-gradient(135deg,#a9b0bb,#5d6470)"></div><small>OUR SERVICES</small><h3>Litigation</h3></div>
  <div class="card" style="left:788px"><div class="card-photo" role="img" aria-label="Legal concept with justice symbols" style="background:linear-gradient(135deg,#9bb2d1,#2c4a7c)"></div><small>OUR SERVICES</small><h3>Collection Claims</h3></div>
  <div class="tagline">The demanded experts in your area</div>
  <div class="btn-white">Contact us
    <svg width="26" height="18" viewBox="0 0 26 18"><path d="M0 9h23M16 2l7 7-7 7" stroke="#1c6c8c" stroke-width="2.5" fill="none"/></svg></div>
</section>

<section class="about">
  <div class="about-bg" role="img" aria-label="Office meeting in the background"></div>
  <div class="about-shade"></div>
  <div class="back-card"></div>
  <div class="about-photo" role="img" aria-label="Two lawyers reviewing a tablet together"></div>
  <div class="about-text" style="top:60px;font-size:13px;font-weight:500;text-decoration:underline;text-underline-offset:4px">WHO WE ARE</div>
  <h2 class="about-text" style="top:95px">Turning Challenges into<br>Legal Triumphs</h2>
  <div class="about-text head" style="top:222px;font-size:21px;font-weight:500">Legal Precision, Client Success</div>
  <p class="about-text" style="top:270px;width:495px;font-size:13.5px;line-height:20.5px">Lorem ipsum dolor sit amet, consectetur adipiscing elit, sed do eiusmod tem por incididunt ut labore et dolore magna aliqua. Ut enim ad minim veniam, q uis nostrud exercitation ullamco laboris nisi ut aliquip ex ea commodo consequat. Duis aute irure dolor in reprehenderit in voluptate velit esse cillum dolore eu fugiat nulla pariatur. Excepteur sint occaecat cupidatat non proident, sunt in culpa qui officia deserunt mollit.</p>
  <div class="btn-red" style="left:608px;top:431px;width:156px;height:41px">Contact us
    <svg width="18" height="12" viewBox="0 0 18 12"><path d="M0 6h16M11 1l5 5-5 5" stroke="#fff" stroke-width="2" fill="none"/></svg></div>
</section>

<section class="why">
  <div class="label" style="top:66px">WHY US</div>
  <h2 class="title" style="top:100px">Why Choose Us</h2>
  <div class="ring" style="left:398px;top:193px;width:404px;height:404px;border:2px solid #d9dcec"></div>
  <div class="ring" style="left:420px;top:215px;width:360px;height:360px;background:var(--lavender)"></div>
  <div class="ring" style="left:434px;top:229px;width:332px;height:332px;background:#fff"></div>
  <div class="abs" role="img" aria-label="Smiling businesswoman with crossed arms" style="left:460px;top:187px;width:280px;height:380px;border-radius:140px 140px 140px 140px/140px 140px 150px 150px;background:linear-gradient(180deg,#d9c7b4 0%,#b9a58f 35%,#1c2437 60%,#141a28 100%)"></div>
  <div class="feat-icon" style="left:441px;top:329px"><svg width="24" height="24" viewBox="0 0 24 24" fill="none" stroke="#fff" stroke-width="2"><circle cx="12" cy="4" r="2"/><path d="M3 9h18M12 9v6l-5 7M12 15l5 7"/></svg></div>
  <div class="feat-icon" style="left:759px;top:329px"><svg width="24" height="24" viewBox="0 0 24 24" fill="none" stroke="#fff" stroke-width="2"><circle cx="12" cy="12" r="9"/><circle cx="12" cy="12" r="4"/></svg></div>
  <div class="feat-icon" style="left:416px;top:429px"><svg width="24" height="24" viewBox="0 0 24 24" fill="none" stroke="#fff" stroke-width="2" stroke-dasharray="3 3"><circle cx="12" cy="12" r="9"/></svg></div>
  <div class="feat-icon" style="left:782px;top:429px"><svg width="24" height="24" viewBox="0 0 24 24" fill="none" stroke="#fff" stroke-width="2"><path d="M4 12a8 8 0 0 1 16 0M20 12a8 8 0 0 1-16 0M8 12h8"/></svg></div>
  <div class="feat-icon" style="left:461px;top:528px"><svg width="24" height="24" viewBox="0 0 24 24" fill="none" stroke="#fff" stroke-width="2"><path d="M4 12a8 8 0 0 1 16 0M20 12a8 8 0 0 1-16 0M8 12h8"/></svg></div>
  <div class="feat-icon" style="left:739px;top:528px"><svg width="24" height="24" viewBox="0 0 24 24" fill="none" stroke="#fff" stroke-width="2"><rect x="3" y="3" width="5" height="5"/><rect x="16" y="16" width="5" height="5"/><path d="M8 5h10v11M16 19H6V8"/></svg></div>
  <div class="feat l" style="left:43px;top:287px"><h4>Client Centric</h4><p>Lorem ipsum dolor sit amet,<br>consectetur adipiscing elit,</p></div>
  <div class="feat l" style="left:21px;top:406px"><h4>Free Consultation</h4><p>Lorem ipsum dolor sit amet,<br>consectetur adipiscing elit,</p></div>
  <div class="feat l" style="left:46px;top:514px"><h4>Minimize Exposure</h4><p>Lorem ipsum dolor sit amet,<br>consectetur adipiscing elit,</p></div>
  <div class="feat" style="left:820px;top:287px"><h4>Attorney Letters</h4><p>Lorem ipsum dolor sit amet,<br>consectetur adipiscing elit,</p></div>
  <div class="feat" style="left:857px;top:406px"><h4>Affordable</h4><p>Lorem ipsum dolor sit amet,<br>consectetur adipiscing elit,</p></div>
  <div class="feat" style="left:820px;top:514px"><h4>Legal Experts</h4><p>Lorem ipsum dolor sit amet,<br>consectetur adipiscing elit,</p></div>
</section>

<section class="reviews">
  <div class="reviews-bg" role="img" aria-label="Business people meeting in the background"></div>
  <div class="reviews-shade"></div>
  <div class="abs" style="left:88px;top:51px;color:#fff;font-size:13px;font-weight:500;text-decoration:underline;text-underline-offset:4px">TESTIMONIALS</div>
  <h2 class="abs head" style="left:88px;top:85px;color:#fff;font-size:44px;font-weight:700">Clients Reviews</h2>
  <div class="abs" style="left:914px;top:102px;color:#fff;font-size:14px;font-weight:500">More Testimonials</div>
  <div class="abs" style="left:1066px;top:91px;width:39px;height:39px;background:var(--red);display:flex;align-items:center;justify-content:center"><svg width="10" height="16" viewBox="0 0 10 16"><path d="M2 2l6 6-6 6" stroke="#fff" stroke-width="2.5" fill="none"/></svg></div>
  <div class="quote" style="left:93px"><h3>Their service was excellent</h3><p>Lorem ipsum dolor sit amet, consectetur adipiscing elit, sed do por incididunt ut labore et dolore magna aliqua. Ut enim ad mi uis nostrud exercitation</p></div>
  <div class="quote" style="left:613px"><h3>Their service was excellent</h3><p>Lorem ipsum dolor sit amet, consectetur adipiscing elit, sed do por incididunt ut labore et dolore magna aliqua. Ut enim ad mi uis nostrud exercitation</p></div>
  <div class="person" style="left:108px"><div class="avatar" role="img" aria-label="Client portrait"></div><div><b>Mara Linden</b><span>Client</span></div></div>
  <div class="person" style="left:628px"><div class="avatar" role="img" aria-label="Client portrait"></div><div><b>Mara Linden</b><span>Client</span></div></div>
</section>

<section class="contact">
  <div class="label" style="top:72px">CONTACT US</div>
  <h2 class="title" style="top:106px">Get in touch with us</h2>
  <div class="contact-foot" role="img" aria-label="Dark office scene behind the footer"></div>
  <svg class="curve" width="1200" height="160" viewBox="0 0 1200 160"><path d="M0 150 Q90 90 200 70 L200 60 Q80 80 0 130Z" fill="#b0121b"/><path d="M1060 70 Q1150 90 1200 130 L1200 170 Q1140 105 1060 90Z" fill="#b0121b"/></svg>
  <div class="contact-card">
    <div class="contact-photo" role="img" aria-label="Two businessmen looking at a tablet"></div>
    <div class="abs" style="left:510px;top:38px;display:flex;align-items:center;gap:10px;font-family:'Ubuntu',sans-serif;font-weight:500;font-size:16px;color:var(--navy)"><span class="dot" style="width:44px;height:44px"></span>Shieldline Legal</div>
    <div class="abs" style="left:510px;top:108px;font-size:30px;font-weight:300;color:var(--navy)">Please fill out the form</div>
    <div class="field" style="left:510px;top:171px;width:360px;height:37px">Name</div>
    <div class="field" style="left:510px;top:225px;width:173px;height:37px">Phone</div>
    <div class="field" style="left:698px;top:225px;width:172px;height:37px">Email</div>
    <div class="field" style="left:510px;top:279px;width:360px;height:68px">Message</div>
    <div class="send">Send</div>
  </div>
  <div class="foot-brand"><span class="dot" style="width:90px;height:90px;background:var(--red);border:4px solid #fff"></span>Shieldline Legal</div>
  <div class="foot-links">
    <a style="left:353px">HOME</a><a style="left:445px">SERVICES</a><a style="left:551px">ABOUT US</a><a style="left:670px">TESTIMONIALS</a><a style="left:821px">BLOG</a>
  </div>
  <div class="foot-rule"></div>
  <div class="foot-item" style="left:172px"><div class="ring-icon"><svg width="28" height="28" viewBox="0 0 28 28" fill="none" stroke="#fff" stroke-width="1.6"><circle cx="14" cy="14" r="11"/><path d="M3 14h22M14 3c-5 6-5 16 0 22M14 3c5 6 5 16 0 22"/></svg></div><div>48 Harbor Lane, Suite 2<br>Ridgeton, ST 40211</div></div>
  <div class="vline" style="left:431px"></div>
  <div class="foot-item" style="left:505px"><div class="ring-icon"><svg width="22" height="28" viewBox="0 0 22 28" fill="none" stroke="#fff" stroke-width="1.6"><rect x="5" y="2" width="12" height="24" rx="2"/><path d="M9 22h4"/></svg></div><div><b>PHONE</b><br>(555) 014 2288</div></div>
  <div class="vline" style="left:750px"></div>
  <div class="foot-item" style="left:826px"><div class="ring-icon"><svg width="28" height="22" viewBox="0 0 28 22" fill="none" stroke="#fff" stroke-width="1.6"><rect x="2" y="2" width="24" height="18" rx="1"/><path d="M2 3l12 9 12-9"/></svg></div><div><b>EMAIL</b><br>hello@shieldline.com</div></div>
</section>

<footer class="bottombar">
  <div class="abs" style="left:147px;top:19px;font-size:13px;font-weight:500">Shieldline Legal</div>
  <i class="soc" style="left:934px"></i><i class="soc" style="left:967px"></i><i class="soc" style="left:1000px"></i><i class="soc" style="left:1033px"></i>
</footer>

</body>
</html>
```